WebSite Revamp / Modernize / stylize to draw in more customers to stay on site

Keel-Deck is looking for a website revamp - we had our old site for some time and now is the time for an update - current site - http://www.keel-deck-example.com/ For additional photos, head to the facebook page - https://www.facebook.com/keeldeckexample / I attached the entire current website as well - looking for something modern and bold that has guy appeal - this is not a cheap product and would like site to have that feel as well.

Target Market(s)

Fishermen, fishing guides, homeowners, boat owners

Coding

Coded - Design and coding required

Number of Pages Required

5+ page

Font styles to use
Serif
Sans Serif
Other font styles liked:
• logo font is "Niamey Medium"

Colors
3176b5
0255a3
3276b5
0692cd
33a6d7
85cae6
cee9f5
b1b1b1
d5d5d5

Requirements
Must have
• Keep colors inline with our logo (blues / greys). Also, need it to be relatively easy to add and remove new locations as they come online - we are franchising and starting to add new locations pretty quickly - need this to be an easy process/update to the site.
Nice to have
• Surprise me

```html
<!DOCTYPE html>
<html lang="en">
<head>
<meta charset="utf-8">
<title>Keel-Deck | High Performance Marine Surfacing</title>
<link rel="stylesheet" href="https://fonts.googleapis.com/css2?family=Montserrat:wght@500;600;700;800&family=Open+Sans:ital,wght@0,400;0,600;1,400&display=swap">
<style>
:root{
  --navy:#0b3a8c;
  --brand:#0255a3;
  --sky:#0692cd;
  --mid:#3176b5;
  --light:#cee9f5;
  --grey:#b1b1b1;
  --line:#d5d5d5;
  --text:#555;
  --ink:#1e1e1e;
  --white:#fff;
}
*{margin:0;padding:0;box-sizing:border-box}
html,body{width:1200px;height:2601px;overflow:hidden;background:var(--white)}
body{position:relative;font-family:"Open Sans",Arial,sans-serif;color:var(--text)}
.abs{position:absolute}
a{color:inherit;text-decoration:none}

/* header */
.site-header{position:absolute;left:0;top:0;width:1200px;height:104px;background:var(--white)}
.brand-name{position:absolute;left:95px;top:30px;font-family:"Montserrat",sans-serif;font-weight:800;font-size:34px;color:var(--navy);letter-spacing:-.5px}
.call-btn{position:absolute;left:947px;top:7px;width:152px;height:47px;border-radius:24px;background:var(--navy);color:var(--white);font-family:"Montserrat",sans-serif;font-weight:700;font-size:15px;display:flex;align-items:center;justify-content:center}
.main-nav{position:absolute;right:100px;top:68px;display:flex;gap:27px;font-family:"Montserrat",sans-serif;font-weight:700;font-size:15px;color:var(--ink);align-items:center}
.main-nav .active{color:var(--sky);font-weight:600}

/* hero */
.hero{position:absolute;left:0;top:104px;width:1200px;height:585px;overflow:hidden}
.hero-photo{position:absolute;inset:0;background:radial-gradient(ellipse at 50% 70%,#6d7278 0%,#4a4f56 45%,#2c3036 100%)}
.hero-curve{position:absolute;left:0;top:0}
.hero-kicker{position:absolute;width:1200px;top:118px;text-align:center;font-family:"Montserrat",sans-serif;font-weight:500;font-size:48px;color:var(--white);letter-spacing:1px}
.hero-title{position:absolute;width:1200px;top:178px;text-align:center;font-family:"Montserrat",sans-serif;font-weight:700;font-size:72px;color:var(--white);letter-spacing:1px;text-shadow:0 2px 6px rgba(0,0,0,.35)}
.hero-sub{position:absolute;width:1200px;top:277px;text-align:center;font-size:26px;line-height:37px;color:var(--white)}
.hero-dots{position:absolute;top:457px;left:0;width:1200px;display:flex;justify-content:center;gap:6px}
.hero-dots span{width:17px;height:17px;border-radius:50%;border:2px solid var(--white)}
.hero-dots span.on{background:var(--white)}

/* welcome */
.welcome-title{position:absolute;top:752px;width:1200px;text-align:center;font-family:"Montserrat",sans-serif;font-weight:800;font-size:38px;color:var(--navy)}
.welcome-copy{position:absolute;left:210px;width:780px;text-align:center;font-size:14.5px;line-height:27px}
.copy-a{top:823px}
.copy-b{top:904px}

/* features */
.feature{position:absolute;width:318px;height:243px;border:1px solid var(--grey);text-align:center}
.feature-icon{position:absolute;left:109px;top:-51px;width:100px;height:100px;border-radius:50%;background:var(--sky);display:flex;align-items:center;justify-content:center}
.feature-title{position:absolute;top:70px;width:100%;font-size:20px;line-height:29px;font-weight:600;color:var(--ink)}
.feature-text{position:absolute;top:137px;left:18px;right:18px;font-size:13.5px;line-height:25px}

/* testimonial */
.testimonial{position:absolute;left:0;top:1777px;width:1200px;height:529px;overflow:hidden}
.testimonial-photo{position:absolute;inset:0;background:linear-gradient(180deg,#1a62b8 0%,#2470c2 55%,#2e7ccb 100%)}
.quote-mark{position:absolute;left:540px;top:0}
.quote-text{position:absolute;left:160px;width:880px;top:135px;text-align:center;font-style:italic;font-size:15.5px;line-height:31px;color:var(--white)}
.quote-name{position:absolute;width:1200px;top:286px;text-align:center;font-family:"Montserrat",sans-serif;font-weight:600;font-size:24px;color:var(--white)}
.slide-arrow{position:absolute;top:178px;width:45px;height:45px;border-radius:50%;background:rgba(255,255,255,.25);display:flex;align-items:center;justify-content:center}

/* footer */
.footer-brand{position:absolute;left:73px;top:2378px;font-family:"Montserrat",sans-serif;font-weight:800;font-size:44px;color:var(--navy);letter-spacing:-.5px}
.footer-head{position:absolute;top:2306px;font-family:"Montserrat",sans-serif;font-weight:600;font-size:19px;color:var(--ink)}
.footer-links{position:absolute;left:432px;top:2344px;list-style:none;font-size:12px;line-height:17.3px;color:var(--text)}
.news-text{position:absolute;left:631px;top:2348px;width:240px;font-size:12px;line-height:21px}
.news-field{position:absolute;left:631px;top:2403px;width:253px;height:30px;border-bottom:1px solid var(--grey);font-size:11.5px;color:#999;padding:6px 12px}
.news-btn{position:absolute;left:631px;top:2448px;width:97px;height:30px;border-radius:15px;background:var(--brand);color:var(--white);font-family:"Montserrat",sans-serif;font-weight:700;font-size:11px;display:flex;align-items:center;justify-content:center}
.social{position:absolute;left:952px;top:2345px;list-style:none}
.social li{display:flex;align-items:center;gap:19px;height:35px;font-size:12px}
.social .dot{width:26px;height:26px;border-radius:50%;border:1px solid var(--grey)}
.footer-rule{position:absolute;left:99px;top:2509px;width:1000px;height:1px;background:var(--line)}
.copyright{position:absolute;top:2542px;width:1200px;text-align:center;font-size:12.5px}
</style>
</head>
<body>

<header class="site-header">
  <div class="brand-name">Keel-Deck</div>
  <a class="call-btn" href="#">CALL US TODAY</a>
  <nav class="main-nav">
    <a class="active" href="#">HOME</a><a href="#">MARINE</a><a href="#">RESIDENTIAL</a><a href="#">CONTACT</a><a href="#">FAQS</a><a href="#">PHOTOS</a><a href="#">TESTIMONIALS</a><a href="#">LINKS</a>
    <svg width="16" height="16" viewBox="0 0 16 16"><circle cx="6.5" cy="6.5" r="4.8" fill="none" stroke="#1e1e1e" stroke-width="2.2"/><line x1="10" y1="10" x2="14.5" y2="14.5" stroke="#1e1e1e" stroke-width="2.4"/></svg>
  </nav>
</header>

<section class="hero">
  <div class="hero-photo" role="img" aria-label="Boat deck finished with speckled granulated rubber surfacing"></div>
  <svg class="hero-curve" width="1200" height="585" viewBox="0 0 1200 585">
    <path d="M0 425 Q600 700 1200 425 L1200 585 L0 585 Z" fill="var(--navy)"/>
    <path d="M0 505 Q600 665 1200 470 L1200 585 L0 585 Z" fill="var(--white)"/>
  </svg>
  <div class="hero-kicker">HIGH PERFORMANCE</div>
  <div class="hero-title">MARINE SURFACING</div>
  <p class="hero-sub">Slip Resistant, Granulated Rubber Marine Surfacing to<br>Revitalize and Renew your Boat Deck</p>
  <div class="hero-dots"><span class="on"></span><span></span><span></span><span></span></div>
</section>

<h1 class="welcome-title">WELCOME TO KEEL-DECK</h1>
<p class="welcome-copy copy-a">Keel-Deck™ is a recycled granulated rubber flooring that is chemically bonded to your boat deck, patio, or any other surface to create an easy to clean, durable, great looking custom surface with unrivaled slip-resistance</p>
<p class="welcome-copy copy-b">Do not spend your hard earned money on surfacing that you will have to replace in a few years. These inferior surfaces such as bed liners, and carpet will lose there slip-resistance over time, decrease resale value, crack and tear over time, and provide no reduction in hull noise</p>

<article class="feature" style="left:99px;top:1092px">
  <div class="feature-icon"><svg width="44" height="50" viewBox="0 0 44 50"><path d="M4 4 H40 V24 C40 36 30 44 22 47 C14 44 4 36 4 24 Z" fill="#fff"/><path d="M13 12 H31 V24 C31 31 26 36 22 38 C18 36 13 31 13 24 Z" fill="var(--sky)"/></svg></div>
  <h3 class="feature-title">Prevents slips, falls<br>and injuries</h3>
  <p class="feature-text">Keel-Deck's slip resistant properties are unrivaled in safety. With our installation and QA processes you will be</p>
</article>
<article class="feature" style="left:440px;top:1092px">
  <div class="feature-icon"><svg width="50" height="40" viewBox="0 0 50 40"><rect x="3" y="8" width="38" height="24" rx="4" fill="none" stroke="#fff" stroke-width="4"/><rect x="43" y="15" width="5" height="10" fill="#fff"/><rect x="9" y="14" width="10" height="12" fill="#fff"/></svg></div>
  <h3 class="feature-title">Lessens<br>Fatigue</h3>
  <p class="feature-text">With the utilization of rubber granules coupled with our proprietary rubber based epoxy, some of the shock</p>
</article>
<article class="feature" style="left:782px;top:1092px">
  <div class="feature-icon"><svg width="52" height="50" viewBox="0 0 52 50" fill="none" stroke="#fff" stroke-width="3"><path d="M30 17 Q34 25 30 33"/><path d="M24 12 Q31 25 24 38"/><path d="M18 7 Q28 25 18 43"/><line x1="40" y1="4" x2="40" y2="46" stroke-width="5"/><path d="M44 8 h4 M44 16 h4 M44 24 h4 M44 32 h4 M44 40 h4" stroke-width="2"/></svg></div>
  <h3 class="feature-title">Dampens hull<br>noise</h3>
  <p class="feature-text">When installed, Keel-Deck™ acts like a muffler, dampening hull noise created in operating all types of boats</p>
</article>
<article class="feature" style="left:270px;top:1427px">
  <div class="feature-icon"><svg width="54" height="46" viewBox="0 0 54 46" fill="#fff"><rect x="22" y="4" width="10" height="8"/><rect x="14" y="12" width="26" height="10"/><path d="M4 22 H50 L43 36 H11 Z"/><path d="M2 41 Q8 37 14 41 T27 41 T40 41 T52 41" fill="none" stroke="#fff" stroke-width="2.5"/></svg></div>
  <h3 class="feature-title">Enhances the appearance<br>and value of your boat</h3>
  <p class="feature-text">Keel-Deck™ looks great installed. We have thousands of color combinations to match, or create a custom color</p>
</article>
<article class="feature" style="left:612px;top:1427px">
  <div class="feature-icon"><svg width="48" height="48" viewBox="0 0 48 48" fill="none" stroke="#fff" stroke-width="6" stroke-linecap="round"><path d="M20 28 L12 36 a6 6 0 0 1 -8 -8 L12 20"/><path d="M28 20 L36 12 a6 6 0 0 1 8 8 L36 28"/><line x1="18" y1="30" x2="30" y2="18"/></svg></div>
  <h3 class="feature-title">Unrivaled<br>durability</h3>
  <p class="feature-text">Stands up to almost anything you can dish out! Keel-Deck™ will last the lifetime of the craft, or deck.</p>
</article>

<section class="testimonial">
  <div class="testimonial-photo" role="img" aria-label="Close-up of a blue rubber-surfaced boat deck"></div>
  <svg class="abs" style="left:0;top:0" width="1200" height="529" viewBox="0 0 1200 529">
    <path d="M0 400 Q600 330 1200 440" fill="none" stroke="#0a3f95" stroke-width="10"/>
  </svg>
  <svg class="quote-mark" width="120" height="92" viewBox="0 0 120 92" fill="#fff">
    <path d="M6 44 C6 20 18 6 44 0 L46 12 C32 16 28 26 28 38 H52 V92 H6 Z"/>
    <path d="M68 44 C68 20 80 6 106 0 L108 12 C94 16 90 26 90 38 H114 V92 H68 Z"/>
  </svg>
  <p class="quote-text">I spent many weeks looking for a deck coating that that met all my specifications. Color and slip prevention were important but I was also looking for something that offered anti fatigue properties. There are several product that offer a few colors and slip prevention but Keel-Deck is the only one that met all my requirements. It was confirmed after a 12 hour trip to Harlan Ridge. Great value, exceptional service and and highly recommended! Thanks Rob...</p>
  <div class="quote-name">Dale Morrow</div>
  <a class="slide-arrow" style="left:54px" href="#"><svg width="14" height="20" viewBox="0 0 14 20"><path d="M11 2 L3 10 L11 18" fill="none" stroke="#fff" stroke-width="3"/></svg></a>
  <a class="slide-arrow" style="left:1101px" href="#"><svg width="14" height="20" viewBox="0 0 14 20"><path d="M3 2 L11 10 L3 18" fill="none" stroke="#fff" stroke-width="3"/></svg></a>
</section>

<footer>
  <div class="footer-brand">Keel-Deck</div>
  <h4 class="footer-head" style="left:432px">INFORMATION</h4>
  <ul class="footer-links"><li>Home</li><li>Marine</li><li>Residential</li><li>Contact</li><li>FAQs</li><li>Photos</li><li>Testimonials</li><li>Links</li></ul>
  <h4 class="footer-head" style="left:631px">NEWSLETTER SUBSCRIPTION</h4>
  <p class="news-text">Register your Email Address to get Information about us</p>
  <div class="news-field">Email Address</div>
  <a class="news-btn" href="#">SUBSCRIBE</a>
  <h4 class="footer-head" style="left:952px">SOCIAL</h4>
  <ul class="social">
    <li><span class="dot"></span>Friendbook</li>
    <li><span class="dot"></span>Chirper</li>
    <li><span class="dot"></span>Searchplus</li>
    <li><span class="dot"></span>Worklink</li>
  </ul>
  <div class="footer-rule"></div>
  <p class="copyright">Copyrights © 2018, Keel-Deck. All rights reserved.</p>
</footer>

</body>
</html>
```